GlowRun Fundraiser

I am looking for a fresh design for the 10th annual GlowRun fundraiser. Green and blue colors need to be incorporated . I attached the current flyer. I would like this flyer for September 20, 2020. This is a fundraiser to help find a cure for NF, nuerofibromatosis.
Updates

We are looking for a fresh look for the 10th annual event

Target Market(s)

Families and individuals of surrounding areas

Colors
0255a3
add136

Requirements
Must have
• Blue and green colors. It is the 10th annual. The logos of RQ CENTER and children’s hospital logo that are shown on the previous flyer I attached
Nice to have
• Eye catching

```html
<!DOCTYPE html>
<html lang="en">
<head>
<meta charset="utf-8">
<title>GlowRun Fundraiser Flyer</title>
<link rel="stylesheet" href="https://fonts.googleapis.com/css2?family=Big+Shoulders+Display:wght@800&family=Amatic+SC:wght@700&family=Fredoka:wght@600;700&family=Gochi+Hand&family=Lato:wght@400;700;900&display=swap">
<style>
  :root {
    --blue: #233a82;
    --blue-bright: #0255a3;
    --green: #4cb848;
    --ink: #1c1c1c;
    --navy: #162544;
    --surround: #3a3a3c;
    --paper: #ffffff;
  }
  * { margin: 0; padding: 0; box-sizing: border-box; }
  html, body { width: 900px; height: 1200px; overflow: hidden; background: var(--surround); }
  .flyer {
    position: absolute; left: 88px; top: 88px; width: 724px; height: 1024px;
    background: var(--paper); overflow: hidden;
  }
  .edge { position: absolute; top: 0; height: 1024px; z-index: 3; }
  .edge-left { left: 0; width: 26px; }
  .edge-right { right: 0; width: 26px; }
  .abs { position: absolute; }
  .center { left: 0; width: 724px; text-align: center; }

  .masthead { left: 0; top: 0; width: 724px; height: 240px; }
  .masthead .annual { font-family: "Gochi Hand", cursive; font-size: 28px; fill: var(--green); }
  .masthead .title { font-family: "Big Shoulders Display", sans-serif; font-weight: 800; font-size: 250px; fill: var(--blue); }
  .masthead .title .alt { fill: var(--green); }
  .masthead .honoree { font-family: "Big Shoulders Display", sans-serif; font-weight: 800; font-size: 54px; fill: var(--green); }

  .tagline {
    top: 232px; font-family: "Amatic SC", sans-serif; font-weight: 700;
    font-size: 50px; line-height: 56px; color: var(--blue); letter-spacing: -0.5px;
  }
  .tagline .cap { color: var(--green); }
  .rule { left: 58px; width: 608px; height: 2px; background: var(--blue); opacity: .8; }
  .date { top: 300px; font-family: "Fredoka", sans-serif; font-weight: 700; font-size: 31px; color: var(--blue); }
  .time { top: 340px; font-family: "Fredoka", sans-serif; font-weight: 700; font-size: 33px; color: var(--blue); }
  .venue { top: 382px; font-family: "Fredoka", sans-serif; font-weight: 600; font-size: 19px; color: var(--blue); }
  .address { top: 409px; font-family: "Fredoka", sans-serif; font-weight: 600; font-size: 18px; color: var(--blue); }
  .headline { top: 462px; font-family: "Gochi Hand", cursive; font-size: 56px; color: var(--green); white-space: nowrap; }
  .activities { top: 526px; font-family: "Gochi Hand", cursive; font-size: 27px; line-height: 32px; color: var(--ink); white-space: nowrap; }
  .activities .gap { display: inline-block; width: 150px; }
  .follow {
    left: 170px; top: 646px; width: 384px; height: 106px;
    border: 5px solid var(--blue); border-radius: 18px; padding: 5px;
  }
  .follow-inner {
    width: 100%; height: 100%; background: var(--blue); border-radius: 12px;
    display: flex; align-items: center; padding-left: 38px; gap: 20px;
  }
  .follow-dot { flex: none; width: 58px; height: 58px; border: 3px solid var(--paper); border-radius: 50%; }
  .follow-text { font-family: "Gochi Hand", cursive; font-size: 40px; line-height: 1; color: var(--paper); letter-spacing: 1px; white-space: nowrap; }
  .contact-note { top: 768px; font-family: "Lato", sans-serif; font-weight: 700; font-size: 15px; line-height: 20px; color: var(--ink); }
  .center-name {
    left: 52px; top: 840px; width: 150px; text-align: center;
    font-family: "Lato", sans-serif; font-weight: 900; font-size: 34px; line-height: 38px; color: var(--navy);
  }
  .contacts {
    left: 228px; top: 838px; width: 244px; text-align: center; white-space: nowrap;
    font-family: "Lato", sans-serif; font-weight: 700; font-size: 15px; line-height: 19.5px; color: var(--ink);
  }
  .hospital-name {
    left: 486px; top: 848px; width: 200px; text-align: center;
    font-family: "Lato", sans-serif; font-weight: 700; font-size: 22px; line-height: 26px; color: var(--ink);
  }
  .footer {
    left: 0; top: 944px; width: 724px; height: 80px; background: var(--surround);
    font-family: "Lato", sans-serif; font-weight: 400; font-size: 12.5px; line-height: 15px;
    color: var(--paper); text-align: center; padding-top: 12px;
  }
</style>
</head>
<body>
<main class="flyer">
  <svg class="edge edge-left" viewBox="0 0 26 1024" preserveAspectRatio="none" aria-hidden="true">
    <path d="M0 0 H22 Q28 32 22 64 T22 128 T22 192 T22 256 T22 320 T22 384 T22 448 T22 512 T22 576 T22 640 T22 704 T22 768 T22 832 T22 896 T22 960 T22 1024 H0 Z" fill="var(--green)"/>
  </svg>
  <svg class="edge edge-right" viewBox="0 0 26 1024" preserveAspectRatio="none" aria-hidden="true">
    <path d="M26 0 H4 Q-2 32 4 64 T4 128 T4 192 T4 256 T4 320 T4 384 T4 448 T4 512 T4 576 T4 640 T4 704 T4 768 T4 832 T4 896 T4 960 T4 1024 H26 Z" fill="var(--blue)"/>
  </svg>

  <svg class="abs masthead" viewBox="0 0 724 240" role="img" aria-label="10th Annual GlowRun — Dylan">
    <text class="annual" transform="translate(76 94) rotate(-90)" text-anchor="middle" x="0" y="-6">10th</text>
    <text class="annual" transform="translate(76 94) rotate(-90)" text-anchor="middle" x="0" y="22">Annual</text>
    <text class="title" x="112" y="222" textLength="452" lengthAdjust="spacingAndGlyphs">GL<tspan class="alt">OW</tspan>RUN</text>
    <text class="honoree" transform="translate(586 144) rotate(90)" text-anchor="middle" x="0" y="0" textLength="150" lengthAdjust="spacingAndGlyphs">DYLAN</text>
  </svg>

  <p class="abs center tagline"><span class="cap">D</span>onate <span class="cap">Y</span>our <span class="cap">L</span>ove <span class="cap">A</span>gainst <span class="cap">N</span>eurofibromatosis</p>
  <div class="abs rule" style="top:294px"></div>

  <p class="abs center date">Saturday September 20, 2020</p>
  <p class="abs center time">12pm-6pm</p>
  <p class="abs center venue">Maple County Fair Grounds</p>
  <p class="abs center address">214 W. Orchard RD. Millbrook, IL 62400</p>
  <div class="abs rule" style="top:446px"></div>

  <h2 class="abs center headline">Food, Drinks, Music &amp; Fun!!!</h2>
  <p class="abs center activities">
    Kids Games, Bounce House, Face Painting,<br>
    Silent &amp; Live Auction, Bake Sale, Raffles<br>
    Childre's Special by<span class="gap"></span>12-2 walk-in appts
  </p>

  <div class="abs follow">
    <div class="follow-inner">
      <span class="follow-dot"></span>
      <span class="follow-text">Follow us on</span>
    </div>
  </div>

  <p class="abs center contact-note">if anyone wishes to donated any items or purchase a ticket,<br>please contact one of the following people</p>

  <div class="abs center-name">RQ CENTER</div>
  <p class="abs contacts">
    Megan Hale: (555) 201-4478<br>
    Carla Benton: (555) 318-9062<br>
    Julie Prescott: (555) 246-7315<br>
    Dana Whitfield: (555) 246-8820
  </p>
  <div class="abs hospital-name">Riverbend Children's Hospital</div>

  <footer class="abs footer">
    All Proceeds donated to Riverbend Children's Hospital Foundation/Lakeview University RQ Center to help find a cure!<br>
    Sponsored by Family &amp; Friends of D.Y.L.A.N
  </footer>
</main>
</body>
</html>
```